Business Card Design

I am nail technician working from home in Fernwick Rise, Perth and I require new business cards. I only work with Gel medium for nail extensions using tips or I can also do sculpture nails. I specialise in hand painted nail art using water based acrylic paint and nail polish. As the name suggest I love all things "Shimmer" so I would love something that reflects this while also being professional. I'm also on Chatterly and would the Chatterly logo.

Contact Information for Business Card

Shimmer Bay nail designs,Rosanne ,0417859263, ShimmerBaynaildesigns@quellmail.com, nail technician specialising in hand painted nail art, only using a Gel medium

```html
<!DOCTYPE html>
<html lang="en">
<head>
<meta charset="utf-8">
<title>Shimmer Bay nail designs – Business Card</title>
<link rel="stylesheet" href="https://fonts.googleapis.com/css2?family=Open+Sans:wght@400;500&display=swap">
<style>
  :root {
    --brand-red: #e3001b;
    --card-white: #ffffff;
    --edge-grey: #d9d9d9;
  }
  html, body {
    margin: 0;
    padding: 0;
    overflow: hidden;
    background: var(--card-white);
  }
  .business-card {
    position: relative;
    width: 1200px;
    height: 741px;
    overflow: hidden;
    background: var(--card-white);
    font-family: "Open Sans", sans-serif;
    color: var(--brand-red);
  }
  .card-shapes {
    position: absolute;
    inset: 0;
    width: 1200px;
    height: 741px;
  }
  .card-shapes .accent { fill: var(--brand-red); }
  .card-shapes .edge-red { stroke: var(--brand-red); stroke-width: 1.5; }
  .card-shapes .edge-grey { stroke: var(--edge-grey); stroke-width: 1; }
  .card-line {
    position: absolute;
    margin: 0;
    line-height: 1;
    white-space: nowrap;
    font-weight: 400;
  }
  .business-name {
    right: 74px;
    top: 73px;
    font-size: 56px;
  }
  .owner-name {
    right: 82px;
    top: 211px;
    font-size: 90px;
    font-weight: 500;
  }
  .phone {
    right: 82px;
    top: 325px;
    font-size: 47px;
  }
  .email {
    right: 76px;
    top: 392px;
    font-size: 45px;
  }
  .tagline {
    position: absolute;
    left: 408px;
    width: 400px;
    top: 606px;
    margin: 0;
    font-size: 32px;
    line-height: 43px;
    text-align: center;
    white-space: nowrap;
    display: flex;
    flex-direction: column;
    align-items: center;
  }
</style>
</head>
<body>
  <div class="business-card">
    <svg class="card-shapes" viewBox="0 0 1200 741" aria-hidden="true">
      <polygon class="accent" points="17,16 458,16 17,635"/>
      <polygon class="accent" points="1195,454 1195,725 1001,725"/>
      <line class="edge-red" x1="17.5" y1="16" x2="17.5" y2="725"/>
      <line class="edge-grey" x1="17" y1="725.5" x2="1001" y2="725.5"/>
    </svg>

    <h1 class="card-line business-name">Shimmer Bay nail designs</h1>
    <p class="card-line owner-name">Rosanne</p>
    <p class="card-line phone">0417859263</p>
    <p class="card-line email">ShimmerBaynaildesigns@quellmail.com</p>

    <p class="tagline">
      <span>Nail technician specialising in hand painted nail art,</span>
      <span>only using a Gel medium</span>
    </p>
  </div>
</body>
</html>
```